Franchise Brochure

We would like a brochure advertising our company to possible franchisees. Our business is a football(soccer) retail store in Australia.

The brochure should excite the reader with the opportunity of becoming a Pitchside Harbor franchisee. Some major points to include;
* turn a passion into a profession
* growth industry
* major partners include Varlo and Quenby
* Australia's most exciting and unique football retailer
* Specialising in the player, supporter and club
* Lifestyle choice
* Limited Sites available

* Franchisee: Work for yourself, but not by youself

Corporate colours :PMS 260C

include information and pictures from the attachments.
Updates

Project Deadline Extended
Reason: Now guaranteeing payment - one more week to submit designs.

Industry/Entity Type

Advertising

```html
<!DOCTYPE html>
<html lang="en">
<head>
<meta charset="utf-8">
<title>Pitchside Harbor – Franchise Brochure</title>
<link rel="stylesheet" href="https://fonts.googleapis.com/css2?family=Exo+2:ital,wght@0,300;0,400;0,600;0,700;1,600;1,700&family=Kaushan+Script&display=swap">
<style>
  :root {
    --brand-purple: #5b2d86;
    --deep-purple: #2a1540;
    --night: #0d0a12;
    --ink: #3a3a3a;
    --paper: #f4f3f5;
    --paper-shade: #e4e2e7;
    --gold: #f2c200;
    --white: #ffffff;
    --lilac: #c9b3e6;
    --stage: #ffffff;
  }
  * { box-sizing: border-box; margin: 0; padding: 0; }
  html, body { width: 786px; height: 1200px; overflow: hidden; background: var(--stage); }
  body { position: relative; font-family: "Exo 2", sans-serif; color: var(--ink); }

  .page-set { position: absolute; box-shadow: 0 6px 18px rgba(0,0,0,.25); overflow: hidden; }

  /* brand lockup */
  .brand { display: flex; flex-direction: column; align-items: center; gap: 3px; }
  .brand-name { font-family: "Exo 2", sans-serif; font-weight: 700; color: var(--white); font-size: 22px; letter-spacing: .3px; line-height: 1.1; }
  .brand-tagline { font-family: "Exo 2", sans-serif; font-weight: 600; font-style: italic; font-size: 10px; color: var(--lilac); }

  /* cover */
  .front-cover { left: 193px; top: 20px; width: 400px; height: 280px; }
  .cover-photo { position: absolute; inset: 0; background: radial-gradient(ellipse at 60% 35%, #8a66b8 0%, #4b2a74 45%, #1e0f2e 100%); }
  .front-cover .brand { position: absolute; left: 22px; top: 62px; align-items: flex-start; }

  /* spreads */
  .spread { left: 20px; width: 746px; height: 250px; display: flex; background: var(--paper); }
  .spread-welcome { top: 320px; }
  .spread-support { top: 590px; }
  .page { position: relative; width: 373px; height: 100%; overflow: hidden; }
  .page-left { border-right: 1px solid var(--paper-shade); }

  .net-photo { position: absolute; left: 0; top: 0; width: 100%; height: 150px; background: radial-gradient(circle at 62% 40%, #6d6a78 0%, #3b2a55 35%, #170c24 85%); }
  .spread-welcome .brand { position: absolute; left: 16px; top: 34px; align-items: flex-start; }
  .welcome-band { position: absolute; left: 0; bottom: 0; width: 100%; height: 100px; background: var(--night); padding: 12px 16px; }
  .welcome-band h2 { font-style: italic; font-weight: 700; font-size: 15px; color: var(--gold); margin-bottom: 5px; }
  .welcome-band p { font-size: 7px; line-height: 1.45; color: #cfcad6; font-weight: 300; }

  .opportunity { padding: 14px 18px 0; }
  .section-title { font-style: italic; font-weight: 700; color: var(--brand-purple); font-size: 13px; margin-bottom: 3px; }
  .opportunity p { font-size: 8px; line-height: 1.4; margin-bottom: 7px; }
  .expertise-list { list-style: none; font-size: 8px; line-height: 1.6; }
  .expertise-list li::before { content: ""; display: inline-block; width: 4px; height: 4px; border-radius: 50%; background: var(--brand-purple); margin-right: 6px; vertical-align: middle; }
  .passion-band { position: absolute; left: 0; bottom: 0; width: 100%; height: 90px; background: var(--night); }
  .passion-strip { position: absolute; left: 0; top: 0; width: 100%; height: 26px; background: linear-gradient(90deg, #2b1b40, #4a3566 50%, #241432); }
  .passion-line { position: absolute; left: 22px; top: 44px; font-family: "Kaushan Script", cursive; font-size: 19px; color: var(--white); }
  .passion-line em { font-style: normal; color: var(--gold); }

  /* support spread */
  .support-copy { padding: 12px 16px 0; }
  .support-copy .section-title { font-size: 12px; margin-bottom: 2px; }
  .support-copy p { font-size: 7.4px; line-height: 1.42; margin-bottom: 7px; }
  .marketing-block { display: flex; gap: 8px; align-items: flex-start; }
  .marketing-block p { width: 190px; position: relative; z-index: 1; }
  .store-photo { width: 84px; height: 62px; margin-left: auto; background: linear-gradient(160deg, #b74a52, #6e4d6a 50%, #d9cfd9); border: 2px solid var(--white); position: relative; z-index: 1; }
  .corner-wedge { position: absolute; right: 0; bottom: 0; width: 150px; height: 120px; background: var(--night); clip-path: polygon(100% 0, 100% 100%, 0 100%); }

  .success-copy { padding: 14px 18px 0; }
  .success-copy p { font-size: 7.6px; line-height: 1.45; }
  .partners-band { position: absolute; left: 0; bottom: 0; width: 100%; height: 118px; background: var(--night); padding: 12px 16px; }
  .partners-band h3 { font-style: italic; font-weight: 600; font-size: 10px; color: var(--gold); }
  .partner-row { display: flex; justify-content: space-around; align-items: center; margin-top: 30px; }
  .partner-name { font-family: "Exo 2", sans-serif; font-weight: 700; font-size: 22px; color: var(--white); }

  /* back cover */
  .back-cover { left: 193px; top: 870px; width: 400px; height: 280px; }
  .pitch-photo { position: absolute; inset: 0; background: radial-gradient(ellipse at 40% 20%, #3a2450 0%, #1c1026 55%, #0c0712 100%); }
  .back-cover .brand { position: absolute; left: 0; right: 0; bottom: 40px; }
</style>
</head>
<body>

<section class="page-set front-cover">
  <div class="cover-photo" role="img" aria-label="Purple-toned photo of a player striking a football mid-air beside a goalpost"></div>
  <div class="brand">
    <span class="brand-name">Pitchside Harbor</span>
    <span class="brand-tagline">"Your home ground for the game"</span>
  </div>
</section>

<section class="page-set spread spread-welcome">
  <div class="page page-left">
    <div class="net-photo" role="img" aria-label="Close-up photo of a football resting in a goal net"></div>
    <div class="brand">
      <span class="brand-name">Pitchside Harbor</span>
      <span class="brand-tagline">"Your home ground for the game"</span>
    </div>
    <div class="welcome-band">
      <h2>Welcome to Pitchside Harbor</h2>
      <p>Pitchside Harbor is a company born to provide the football community with a unique and innovative retail experience. We have become one of the leading football retailers within Australia, offering specialised staff, broad ranges and expert service. Partnering with the biggest brands in world football, we cater to the player, supporter and club, and have built a lasting reputation within the football community.</p>
    </div>
  </div>
  <div class="page page-right">
    <div class="opportunity">
      <h2 class="section-title">Why Join Pitchside Harbor - Franchise Opportunity</h2>
      <p>At Pitchside Harbor we have combined our considerable skills, resources and experience to create an opportunity for people to own and operate a Pitchside Harbor store.</p>
      <h2 class="section-title">Share Our Technical Expertise</h2>
      <ul class="expertise-list">
        <li>60+ years of soccer and business experience</li>
        <li>Comprehensive product range</li>
        <li>Relationships with key suppliers including Varlo, Quenby, etc.</li>
        <li>Business management manuals</li>
        <li>Ongoing business coaching and support</li>
      </ul>
    </div>
    <div class="passion-band">
      <div class="passion-strip" role="img" aria-label="Strip of goal net photo in purple tones"></div>
      <p class="passion-line">Turn a <em>passion</em> into a <em>profession</em>.</p>
    </div>
  </div>
</section>

<section class="page-set spread spread-support">
  <div class="page page-left">
    <div class="corner-wedge"></div>
    <div class="support-copy">
      <h2 class="section-title">Training</h2>
      <p>Pitchside Harbor invests heavily in training you to the required standard. This includes shop floor experience as well as support office operations. You will be trained on all aspects of the football business including products, customer service, financial reporting and marketing.</p>
      <h2 class="section-title">Ongoing Support</h2>
      <p>The Pitchside Harbor Support Office provides leadership throughout the opening process and every week of operation, helping you to be in business for yourself whilst having the access to ongoing support and coaching not normally available as an independent business owner.</p>
      <h2 class="section-title">Marketing &amp; Advertising</h2>
      <div class="marketing-block">
        <p>Pitchside Harbor franchisees pay a marketing levy that allows them to receive system-wide group marketing support, allowing for bigger advertising opportunities and brand development. Both group and local area marketing strategies are developed to ensure that you will become one of the leading football specialists in your area.</p>
        <div class="store-photo" role="img" aria-label="Photo of a store interior with football merchandise displays"></div>
      </div>
    </div>
  </div>
  <div class="page page-right">
    <div class="success-copy">
      <h2 class="section-title">Franchise Success - Join the Team</h2>
      <p>No experience is required - simply combine a passion for customer service and football with business acumen. Owning and operating a Pitchside Harbor store sees you helping customers in one of their favourite recreational activities. It's a great business to be involved in and our products, retail and support office provide all the necessary training and ongoing leadership to support the design, build, opening and operation of your store. All of our products are supplied by well-known suppliers including Varlo, Quenby, etc. This means your team can focus on customer service and retailing.</p>
    </div>
    <div class="partners-band">
      <h3>Major partners include Varlo and Quenby</h3>
      <div class="partner-row">
        <span class="partner-name">Varlo</span>
        <span class="partner-name">Quenby</span>
        <span class="partner-name">Castrel</span>
      </div>
    </div>
  </div>
</section>

<section class="page-set back-cover">
  <div class="pitch-photo" role="img" aria-label="Dark purple photo of a football pitch with white line markings"></div>
  <div class="brand">
    <span class="brand-name">Pitchside Harbor</span>
    <span class="brand-tagline">"Your home ground for the game"</span>
  </div>
</section>

</body>
</html>
```